Drifting Past Solvane website

A very basic website using the graphics provided. The site would give the user the ability to read a description of the book, read testimonials, About the author, Read chapter 1, link to vendoro, order direct via coinlet.

```html
<!DOCTYPE html>
<html lang="en">
<head>
<meta charset="utf-8">
<title>Drifting Past Solvane</title>
<link rel="stylesheet" href="https://fonts.googleapis.com/css2?family=Arimo:wght@400;700&display=swap">
<style>
  :root {
    --maroon-dark: #4f2123;
    --maroon: #8a3639;
    --maroon-shade: #6e2a2d;
    --paper: #d6d6d6;
    --ink: #2e2e2e;
    --ink-strong: #111;
    --white: #ffffff;
    --footer-text: #d9c9c9;
    --vendor: #e8a13a;
    --coin: #1d3f78;
    --cover-dark: #1a1414;
    --cover-mid: #5b3a34;
  }
  * { margin: 0; padding: 0; box-sizing: border-box; }
  html, body { width: 1096px; height: 1200px; overflow: hidden; }
  body {
    font-family: "Arimo", Arial, sans-serif;
    background: var(--paper);
    color: var(--ink);
    position: relative;
  }
  a { color: inherit; text-decoration: none; }

  .site-header {
    position: absolute; left: 0; top: 0; width: 1096px; height: 61px;
    background: var(--maroon-dark);
  }
  .brand {
    position: absolute; left: 113px; top: 17px;
    font-size: 24px; font-weight: 400; color: var(--white);
  }
  .main-nav {
    position: absolute; right: 114px; top: 22px;
    display: flex; gap: 21px; font-size: 15px; color: var(--white);
  }

  .hero {
    position: absolute; left: 0; top: 61px; width: 1096px; height: 346px;
    background: var(--maroon);
  }
  .hero-divider {
    position: absolute; left: 537px; top: 0; width: 3px; height: 346px;
    background: linear-gradient(to bottom, var(--maroon), var(--maroon-shade) 25%, var(--maroon-shade) 75%, var(--maroon));
  }
  .hero-band {
    position: absolute; left: 0; top: 407px; width: 1096px; height: 15px;
    background: var(--maroon-dark);
  }
  .book-stack {
    position: absolute; left: 93px; top: 44px; width: 282px; height: 247px;
  }
  .book-stack .cover {
    position: absolute;
    background: linear-gradient(to bottom, var(--cover-dark), var(--cover-mid) 45%, var(--cover-dark));
    box-shadow: 2px 3px 8px rgba(0,0,0,0.45);
  }
  .cover.back-left { left: 0; top: 0; width: 143px; height: 207px; }
  .cover.back-right { left: 139px; top: 22px; width: 143px; height: 207px; }
  .cover.front { left: 64px; top: 40px; width: 143px; height: 207px; }

  .order {
    position: absolute; left: 590px; top: 93px; width: 460px; text-align: center; color: var(--white);
  }
  .order h2 { font-size: 20px; font-weight: 700; margin-bottom: 10px; }
  .order p { font-size: 13px; line-height: 19px; hyphens: auto; }
  .pay-options {
    display: flex; justify-content: center; align-items: center; gap: 22px;
    margin-top: 34px; margin-left: -4px; font-weight: 700;
  }
  .pay-vendor { font-size: 17px; font-weight: 400; color: var(--vendor); }
  .pay-or { font-size: 15px; color: var(--white); }
  .pay-coin { font-size: 21px; font-weight: 400; color: var(--coin); }

  .info {
    position: absolute; top: 456px; width: 450px;
  }
  .info.author { left: 80px; }
  .info.book { left: 568px; }
  .info h3, .chapter h3 {
    font-size: 24px; font-weight: 700; color: var(--ink-strong); margin-bottom: 8px;
  }
  .info p {
    font-size: 17.5px; line-height: 20.7px; hyphens: auto;
  }

  .chapter {
    position: absolute; left: 80px; top: 758px; width: 936px;
  }
  .chapter-text {
    height: 228px; overflow: hidden;
    font-size: 17.5px; line-height: 20.7px;
  }
  .chapter-cover {
    float: left; width: 107px; height: 156px; margin: 6px 8px 0 2px;
    background: linear-gradient(to bottom, var(--cover-dark), var(--cover-mid) 45%, var(--cover-dark));
  }
  .chapter-text p.narrow { padding-right: 118px; }

  .read-more {
    position: absolute; left: 863px; top: 1044px; width: 154px; height: 47px;
    background: var(--maroon-dark); color: var(--white); border-radius: 5px;
    font-size: 17px; display: flex; align-items: center; justify-content: center;
  }

  .site-footer {
    position: absolute; left: 0; top: 1138px; width: 1096px; height: 62px;
    background: var(--maroon-dark); color: var(--footer-text); font-size: 14px;
  }
  .footer-nav { position: absolute; left: 80px; top: 24px; display: flex; gap: 19px; }
  .copyright { position: absolute; right: 79px; top: 24px; }
</style>
</head>
<body>
  <header class="site-header">
    <a class="brand" href="#">MiloVarrick</a>
    <nav class="main-nav">
      <a href="#order">Order Now</a>
      <a href="#book">About Book</a>
      <a href="#author">About Author</a>
    </nav>
  </header>

  <section class="hero" id="order">
    <div class="book-stack" role="img" aria-label="Three copies of the book Drifting Past Solvane by Milo Varrick, covers showing a silhouette behind bars">
      <div class="cover back-left"></div>
      <div class="cover back-right"></div>
      <div class="cover front"></div>
    </div>
    <div class="hero-divider"></div>
    <div class="order">
      <h2>Order Now!</h2>
      <p>Lorem Ipsum is simply dummy text of the printing and typesetting industry. Lorem Ipsum has been the industry's standard dummy text ever since the 1500s, when an unknown printer took a galley of type and scrambled</p>
      <div class="pay-options">
        <a class="pay-vendor" href="#">vendoro</a>
        <span class="pay-or">OR</span>
        <a class="pay-coin" href="#">coinlet</a>
      </div>
    </div>
  </section>
  <div class="hero-band"></div>

  <section class="info author" id="author">
    <h3>About Milo Varrick</h3>
    <p>Lorem Ipsum is simply dummy text of the printing and typesetting industry. Lorem Ipsum has been the industry's standard dummy text ever since the 1500s, when an unknown printer took a galley of type and scrambled it to make a type specimen book. It has survived not only five centuries, but also the leap into electronic typesetting, remaining essentially unchanged. It was popularised in the 1960s with the release of Typeleaf sheets containing Lorem Ipsum passages, and more recently with desktop publishing software like Pagecraft including versions of Lorem Ipsum.</p>
  </section>

  <section class="info book" id="book">
    <h3>About Book</h3>
    <p>Lorem Ipsum is simply dummy text of the printing and typesetting industry. Lorem Ipsum has been the industry's standard dummy text ever since the 1500s, when an unknown printer took a galley of type and scrambled it to make a type specimen book. It has survived not only five centuries, but also the leap into electronic typesetting, remaining essentially unchanged. It was popularised in the 1960s with the release of Typeleaf sheets containing Lorem Ipsum passages, and more recently with desktop publishing software like Pagecraft including versions of Lorem Ipsum.</p>
  </section>

  <section class="chapter">
    <h3>Chapter 1</h3>
    <div class="chapter-text">
      <div class="chapter-cover" role="img" aria-label="Book cover of Drifting Past Solvane"></div>
      <p>Lorem Ipsum is simply dummy text of the printing and typesetting industry. Lorem Ipsum has been the industry's standard dummy text ever since the 1500s, when an unknown printer took a galley of type and scrambled it to make a type specimen book. It has survived not only five centuries, but also the leap into electronic typesetting, remaining essentially unchanged. It was popularised in the 1960s with the release of Typeleaf sheets containing Lorem Ipsum passages, and more recently with desktop publishing software like Pagecraft including versions of Lorem Ipsum.</p>
      <p class="narrow">Lorem Ipsum is simply dummy text of the printing and typesetting industry. Lorem Ipsum has been the industry's standard dummy text ever since the 1500s, when an unknown printer took a galley of type and scrambled it to make a type specimen book. It has survived not only five centuries, but also the leap into electronic typesetting, remaining essentially unchanged. It was popularised in the 1960s with the release of Typeleaf sheets containing Lorem Ipsum passages, and more recently with</p>
    </div>
  </section>

  <a class="read-more" href="#">Read more</a>

  <footer class="site-footer">
    <nav class="footer-nav">
      <a href="#order">Order Now</a>
      <a href="#book">About Book</a>
      <a href="#author">About Author</a>
    </nav>
    <p class="copyright">© 2014 Drifting Past Solvane. All rights reserved.</p>
  </footer>
</body>
</html>
```